Child Care Centre needs new roadside billboard / sign*

We have a 2400mm x 1200mm sign that needs to be refreshed. The design is dated and we want to create a new cleaner, more readable roadside signIt needs to be readable from about 100m awayThe text requirements are simple, but we need it to have a warm, family feel.We are located in a small beach side community and we have a lot of bright colours in our centre (a lot of blues and yellows)https://www.saltmarshchildcare.com.au/

Target Market(s)

Parents of young children

Industry/Entity Type

Childcare

Colors
fbed22
0355a3

Requirements
Must have
• Readable from c.100m
• Simple, warm design
Should not have
• Cluttered or overly busy

```html
<!DOCTYPE html>
<html lang="en">
<head>
<meta charset="utf-8">
<title>Saltmarsh Early Education – Roadside Sign</title>
<link rel="stylesheet" href="https://fonts.googleapis.com/css2?family=Archivo:wght@700;800;900&display=swap">
<style>
  :root {
    --cream: #f6ecc4;
    --cream-light: #faf3d8;
    --sun: #fbed22;
    --sun-deep: #f3e04a;
    --blue: #0355a3;
    --ink: #231f20;
    --tick: #e0262b;
    --green: #6cbf6e;
    --green-pale: #bfe0ab;
    --white: #ffffff;
  }
  * { margin: 0; padding: 0; box-sizing: border-box; }
  html, body { width: 1200px; height: 600px; overflow: hidden; background: var(--cream); }
  .sign {
    position: relative;
    width: 1200px;
    height: 600px;
    overflow: hidden;
    font-family: "Archivo", "Arial Black", sans-serif;
    background: radial-gradient(circle at 930px -70px, var(--cream-light) 0, var(--cream) 75%);
  }
  .backdrop { position: absolute; inset: 0; }
  .brand {
    position: absolute;
    left: 70px;
    top: 48px;
    display: flex;
    align-items: center;
    gap: 16px;
  }
  .brand-dot {
    width: 74px; height: 74px;
    border-radius: 50%;
    background: var(--sun);
    flex: none;
  }
  .brand-name {
    color: var(--ink);
    font-weight: 800;
    font-size: 46px;
    line-height: 1.05;
  }
  .brand-name span { display: block; }
  .services {
    position: absolute;
    left: 115px;
    top: 212px;
    list-style: none;
  }
  .service {
    display: flex;
    align-items: flex-start;
    gap: 33px;
    color: var(--ink);
    font-weight: 800;
    font-size: 41px;
    line-height: 54px;
    margin-bottom: 30px;
  }
  .service:last-child { margin-top: 14px; }
  .tick { width: 52px; height: 48px; flex: none; margin-top: 6px; }
  .open {
    position: absolute;
    left: 694px;
    top: 22px;
    color: var(--blue);
    font-weight: 900;
    font-size: 150px;
    letter-spacing: 2px;
    line-height: 1;
  }
  .hours {
    position: absolute;
    left: 724px;
    top: 180px;
    color: var(--blue);
    font-weight: 900;
    font-size: 56px;
    line-height: 1;
    white-space: nowrap;
  }
  .hours small { font-size: 36px; }
  .badge {
    position: absolute;
    left: 940px;
    top: 296px;
    width: 170px;
    height: 170px;
    border-radius: 50%;
    background: var(--white);
    border: 1.5px solid #2aa7e0;
    box-shadow: 4px 3px 0 -1px var(--white), 5px 4px 0 0 var(--tick);
    display: flex;
    flex-direction: column;
    align-items: center;
    justify-content: center;
    color: var(--blue);
    font-weight: 900;
    font-size: 29px;
    line-height: 1.15;
    text-align: center;
  }
  .phone {
    position: absolute;
    left: 586px;
    top: 488px;
    display: flex;
    align-items: center;
    gap: 26px;
    color: var(--ink);
    font-weight: 900;
    font-size: 74px;
    line-height: 1;
    white-space: nowrap;
  }
  .phone-icon { width: 64px; height: 64px; }
</style>
</head>
<body>
<main class="sign">
  <svg class="backdrop" width="1200" height="600" viewBox="0 0 1200 600" aria-hidden="true">
    <circle cx="932" cy="-70" r="486" fill="var(--sun-deep)" opacity="0.5"/>
    <circle cx="932" cy="-70" r="466" fill="var(--sun)"/>
    <circle cx="80" cy="640" r="175" fill="var(--green-pale)"/>
    <path d="M-95 640 A175 175 0 0 1 255 640" fill="none" stroke="var(--green)" stroke-width="12" opacity="0.85"/>
  </svg>

  <header class="brand">
    <div class="brand-dot"></div>
    <h1 class="brand-name"><span>Saltmarsh</span><span>Early Education</span></h1>
  </header>

  <ul class="services">
    <li class="service">
      <svg class="tick" viewBox="0 0 52 48"><rect x="1.5" y="10" width="32" height="32" fill="none" stroke="var(--tick)" stroke-width="2"/><path d="M6 26 L17 36 L48 3" fill="none" stroke="var(--tick)" stroke-width="6" stroke-linecap="round" stroke-linejoin="round"/></svg>
      <span>6 weeks to 6 years<br>(long day care)</span>
    </li>
    <li class="service">
      <svg class="tick" viewBox="0 0 52 48"><rect x="1.5" y="10" width="32" height="32" fill="none" stroke="var(--tick)" stroke-width="2"/><path d="M6 26 L17 36 L48 3" fill="none" stroke="var(--tick)" stroke-width="6" stroke-linecap="round" stroke-linejoin="round"/></svg>
      <span>Before and After<br>School Care</span>
    </li>
    <li class="service">
      <svg class="tick" viewBox="0 0 52 48"><rect x="1.5" y="10" width="32" height="32" fill="none" stroke="var(--tick)" stroke-width="2"/><path d="M6 26 L17 36 L48 3" fill="none" stroke="var(--tick)" stroke-width="6" stroke-linecap="round" stroke-linejoin="round"/></svg>
      <span>Vacation Care</span>
    </li>
  </ul>

  <h2 class="open">OPEN</h2>
  <p class="hours">6.30<small>AM</small> – 6.30<small>PM</small></p>

  <div class="badge"><span>52</span><span>WEEKS</span><span>A YEAR</span></div>

  <p class="phone">
    <svg class="phone-icon" viewBox="0 0 64 64" aria-hidden="true">
      <path d="M14 22 c-4 10 4 28 18 36 l6 -8 c1 -2 0 -3 -2 -4 l-6 -3 c-2 -1 -3 0 -4 1 c-5 -3 -9 -11 -9 -16 c2 0 3 -1 3 -3 l-1 -7 c0 -2 -2 -3 -4 -2 z" fill="var(--ink)"/>
      <path d="M34 22 a10 10 0 0 1 8 10" fill="none" stroke="#2aa7e0" stroke-width="4" stroke-linecap="round"/>
      <path d="M36 12 a20 20 0 0 1 16 20" fill="none" stroke="#2aa7e0" stroke-width="4" stroke-linecap="round"/>
      <path d="M38 2 a30 30 0 0 1 24 30" fill="none" stroke="#2aa7e0" stroke-width="4" stroke-linecap="round"/>
    </svg>
    <span>07 4150 2286</span>
  </p>
</main>
</body>
</html>
```